Wine Label for a Sweet Wine Called "Glimmora"

We need a wine label that will be used for both a sweet red and a sweet white wine. The very important thing to remember is the target market for these wines is: young American women who love sweet wines and they also spend a lot of their money on their hair, clothes, jewelry, nails. They LOVE Glimmora (Glimmora is a word used to describe flashy accessories, jewelry, decoration.) This label needs to be eye catching, showy, fun, glittery. Please put the brand name, "Glimmora," big, and then in smaller but still readable words underneath the label or somewhere on the label: Sweet, Sophisticated, Red (or white). (An example of what I mean is attached). To differentiate between the two color wines you can suggest color changes to differentiate between the red label and the white label but the label design itself should be the same. Ultimately, the label can be the exact same label for both white and red as long as it looks good on a white wine (a greenish/yellow wine in a clear glass bottle) and a red wine (a dark color wine in a dark bottle).

I've attached an example of the text size relationship between the word Glimmora and the words to go underneath or elsewhere on the label, but you can certainly play with this-- it is just a suggestion of the text size relationship, and definitely NOT at all mandatory that you use any of these fonts.

You can pick the size of the label but try to stay within normal wine label sizes, meaning don't go bigger than approx. 3.5 inches wide and 5 inches tall.

Target Market(s)

Young American women who love sweet wines and spend a lot of money on their hair, clothes, jewelry, nails. They love Glimmora (Glimmora is a word that means flashy accessories, jewelry, decoration)

Requirements
Must have
• It needs to be flashy, glittery, fun, eye catching, memorable
Nice to have
• It shouldn't be too too ultra feminine! The target market is strong independent women and we also have men who will buy it too.

```html
<!DOCTYPE html>
<html lang="en">
<head>
<meta charset="UTF-8">
<title>Glimmora Wine Labels</title>
<link href="https://fonts.googleapis.com/css2?family=Playfair+Display:wght@900&family=Josefin+Sans:wght@300;400&display=swap" rel="stylesheet">
<style>
  :root {
    --backdrop-light: #ddd6a8;
    --backdrop-mid: #8f8a6a;
    --backdrop-dark: #120709;
    --panel-black: #000000;
    --type-white: #ffffff;
    --gold-deep: #2a1a06;
    --gold-mid: #a8741a;
    --gold-bright: #e8b838;
    --gold-pale: #f4e07a;
    --olive-dark: #2c2a0c;
  }
  html, body {
    margin: 0;
    padding: 0;
    width: 1200px;
    height: 929px;
    overflow: hidden;
  }
  .board {
    position: relative;
    width: 1200px;
    height: 929px;
    background: linear-gradient(90deg,
      var(--backdrop-light) 0%,
      var(--backdrop-light) 38%,
      var(--backdrop-mid) 52%,
      #3a2c28 64%,
      var(--backdrop-dark) 76%,
      var(--backdrop-dark) 100%);
  }
  .label {
    position: absolute;
    top: 135px;
    width: 461px;
    height: 659px;
    box-shadow: 6px 8px 10px rgba(0, 0, 0, 0.35);
  }
  .label--white { left: 94px; }
  .label--red { left: 636px; top: 133px; height: 661px; box-shadow: none; }

  .label__glitter {
    position: absolute;
    inset: 0;
  }
  .label--white .label__glitter {
    background:
      radial-gradient(ellipse 60% 30% at 75% 8%, rgba(244, 224, 122, 0.85), transparent 70%),
      radial-gradient(ellipse 70% 35% at 70% 80%, rgba(232, 184, 56, 0.75), transparent 70%),
      radial-gradient(ellipse 40% 50% at 95% 50%, rgba(232, 184, 56, 0.7), transparent 70%),
      radial-gradient(ellipse 40% 30% at 10% 90%, rgba(168, 116, 26, 0.45), transparent 70%),
      linear-gradient(160deg, var(--gold-deep) 0%, #140b02 45%, var(--gold-mid) 100%);
  }
  .label--red .label__glitter {
    background:
      radial-gradient(ellipse 50% 35% at 25% 12%, rgba(255, 250, 200, 0.9), transparent 70%),
      radial-gradient(ellipse 55% 30% at 30% 85%, rgba(255, 245, 180, 0.85), transparent 70%),
      radial-gradient(ellipse 45% 35% at 80% 12%, rgba(232, 184, 56, 0.8), transparent 70%),
      radial-gradient(ellipse 45% 35% at 85% 85%, rgba(232, 170, 50, 0.8), transparent 70%),
      linear-gradient(180deg, var(--gold-bright) 0%, var(--olive-dark) 50%, var(--gold-bright) 100%);
  }

  .label__panel {
    position: absolute;
    left: 22px;
    top: 139px;
    width: 417px;
    height: 278px;
    background: var(--panel-black);
    display: flex;
    flex-direction: column;
    align-items: center;
    color: var(--type-white);
  }
  .label__brand {
    margin: 78px 0 0;
    font-family: "Playfair Display", serif;
    font-weight: 900;
    font-size: 84px;
    line-height: 1;
    letter-spacing: -1px;
  }
  .label__tagline {
    margin: 32px 0 0;
    font-family: "Josefin Sans", sans-serif;
    font-weight: 400;
    font-size: 16px;
    letter-spacing: 4px;
    white-space: nowrap;
  }
  .label__divider {
    display: inline-block;
    width: 1px;
    height: 16px;
    background: var(--type-white);
    margin: 0 8px 0 4px;
    vertical-align: -2px;
  }
</style>
</head>
<body>
  <main class="board">
    <article class="label label--white">
      <div class="label__glitter" role="img" aria-label="Gold glitter bokeh sparkles on a black background"></div>
      <div class="label__panel">
        <h1 class="label__brand">Glimmora</h1>
        <p class="label__tagline">SWEET<span class="label__divider"></span>WHITE<span class="label__divider"></span>SOPHISTICATED</p>
      </div>
    </article>

    <article class="label label--red">
      <div class="label__glitter" role="img" aria-label="Bright golden bokeh lights with starburst sparkle lines"></div>
      <div class="label__panel">
        <h2 class="label__brand">Glimmora</h2>
        <p class="label__tagline">SWEET<span class="label__divider"></span>RED<span class="label__divider"></span>SOPHISTICATED</p>
      </div>
    </article>
  </main>
</body>
</html>
```